Business Card Design

We need a business card designed to portray the message that we are wedding and event stylists. We set up garden ceremonies and style wedding reception venues with chair covers and sashes, backdrops and draping's, wishing wells, tealight holders, table centerpieces. We also style corporate functions - Christmas parties, gala dinners, school formals, award nights. The colour of our uniforms are black and hot pink, if these colours could be incorporated. We would like to be able to use this design for letterhead, flyers and postcards etc. We would like the design to portray a professional, classic image that would relate to both spectrums of our business, weddings and corporate events. If you could develop a logo to incorporate would be great

Target Market(s)

brides, corporate compaines

Industry/Entity Type

Wedding

Contact Information for Business Card

Velvet Aisle & Function Rentals
Phone: 0413 586 190 Email:vaafr@quokkamail.com
Web: www.velvetaisleandfunctions.com.au

Requirements
Must have
• Must include that we set up for weddings, engagements, birthdays, anniversaries, corporate functions, school formals, any occasion.

```html
<!DOCTYPE html>
<html lang="en">
<head>
<meta charset="utf-8">
<title>Velvet Aisle &amp; Function Rentals — Business Card</title>
<link rel="stylesheet" href="https://fonts.googleapis.com/css2?family=Pinyon+Script&family=Questrial&family=Mulish:wght@800&display=swap">
<style>
  :root {
    --ink: #0a0a0a;
    --hot-pink: #c8235f;
    --stage: #e9e6e2;
    --warm-dark: #5a3712;
    --warm-light: #d9a55a;
    --warm-gold: #8a5a1c;
    --venue-sky: #c9d3d6;
    --venue-green: #6f7d55;
    --venue-cloth: #e8eaef;
    --room-wall: #d8d3ca;
    --room-table: #f1f0ec;
    --room-floor: #b9ab8e;
  }
  * { margin: 0; padding: 0; box-sizing: border-box; }
  html, body { width: 1200px; height: 1000px; overflow: hidden; }
  body {
    background: var(--stage);
    position: relative;
    font-family: "Questrial", "Century Gothic", sans-serif;
  }
  .card {
    position: absolute;
    left: 180px;
    width: 840px;
    height: 460px;
    border-radius: 34px;
    overflow: hidden;
    background: var(--ink);
  }
  .card--front { top: 20px; }
  .card--back { top: 510px; }
  .card--front svg { display: block; }
  .brand-script {
    font-family: "Pinyon Script", cursive;
    font-size: 50px;
    fill: var(--hot-pink);
  }

  .back-title {
    position: absolute;
    top: 40px;
    left: 60px;
    right: 40px;
    text-align: center;
    font-family: "Mulish", "Century Gothic", sans-serif;
    font-weight: 800;
    font-size: 36px;
    letter-spacing: 0.5px;
    color: var(--hot-pink);
    white-space: nowrap;
  }
  .setup-heading {
    position: absolute;
    top: 148px;
    left: 0;
    right: 0;
    text-align: center;
    font-size: 22px;
    color: var(--hot-pink);
    letter-spacing: 0.5px;
  }
  .occasions {
    position: absolute;
    top: 188px;
    left: 40px;
    right: 40px;
    display: flex;
    justify-content: space-between;
    align-items: flex-start;
    color: var(--hot-pink);
    font-size: 21px;
    line-height: 1.15;
  }
  .occasions__col--left { text-align: left; width: 220px; }
  .occasions__col--mid { text-align: center; width: 210px; padding-top: 18px; }
  .occasions__col--right { text-align: right; width: 260px; padding-top: 44px; }
  .occasions__rule {
    width: 3px;
    height: 52px;
    background: var(--hot-pink);
    margin-top: 30px;
  }
  .occasions__rule--second { margin-top: 50px; }
  .contact-strip {
    position: absolute;
    left: 0;
    right: 0;
    top: 350px;
    height: 36px;
    background: var(--hot-pink);
    display: flex;
    align-items: center;
    gap: 18px;
    padding-left: 28px;
    color: var(--ink);
    font-size: 18px;
    white-space: nowrap;
  }
  .contact-strip__item { display: flex; align-items: center; gap: 6px; }
  .contact-strip svg { display: block; }
</style>
</head>
<body>

<section class="card card--front" aria-label="Card front">
  <svg width="840" height="460" viewBox="0 0 840 460">
    <defs>
      <clipPath id="photo-window">
        <path d="M0,372 C50,200 160,70 312,0 L840,0 L840,100 C830,260 720,400 530,460 L0,460 Z"/>
      </clipPath>
      <linearGradient id="warm" x1="0" y1="0" x2="1" y2="1">
        <stop offset="0" stop-color="var(--warm-dark)"/>
        <stop offset="0.5" stop-color="var(--warm-light)"/>
        <stop offset="1" stop-color="var(--warm-gold)"/>
      </linearGradient>
      <linearGradient id="venue" x1="0" y1="0" x2="0" y2="1">
        <stop offset="0" stop-color="var(--venue-sky)"/>
        <stop offset="0.55" stop-color="var(--venue-green)"/>
        <stop offset="1" stop-color="var(--venue-cloth)"/>
      </linearGradient>
      <linearGradient id="room" x1="0" y1="0" x2="0" y2="1">
        <stop offset="0" stop-color="var(--room-wall)"/>
        <stop offset="0.6" stop-color="var(--room-table)"/>
        <stop offset="1" stop-color="var(--room-floor)"/>
      </linearGradient>
    </defs>
    <g clip-path="url(#photo-window)">
      <rect class="photo photo--candles" x="0" y="0" width="410" height="260" fill="url(#warm)" role="img" aria-label="Photo of candlelit reception table with glassware and chair covers"/>
      <rect class="photo photo--garden-venue" x="410" y="0" width="430" height="200" fill="url(#venue)" role="img" aria-label="Photo of venue with set tables, blue napkins and garden view"/>
      <rect class="photo photo--conference" x="0" y="260" width="840" height="200" fill="url(#room)" role="img" aria-label="Photo of corporate function room with long white tables"/>
      <polygon class="title-band" points="0,255 840,170 840,255 0,340" fill="var(--ink)"/>
    </g>
    <path class="swoosh swoosh--left" d="M0,400 C46,215 150,78 300,0 L330,0 C176,74 62,210 12,410 Z" fill="var(--hot-pink)"/>
    <path class="swoosh swoosh--right" d="M840,82 C836,260 730,410 520,462 L480,462 C700,400 822,262 826,96 Z" fill="var(--hot-pink)"/>
    <text class="brand-script" x="110" y="310" textLength="640" lengthAdjust="spacingAndGlyphs" transform="rotate(-6 110 310)">Velvet Aisle &amp; Function Rentals</text>
  </svg>
</section>

<section class="card card--back" aria-label="Card back">
  <h1 class="back-title">VELVET AISLE &amp; FUNCTION RENTALS</h1>
  <p class="setup-heading">WE SET UP FOR</p>
  <div class="occasions">
    <p class="occasions__col occasions__col--left">weddings,<br>corporate functions,</p>
    <span class="occasions__rule"></span>
    <p class="occasions__col occasions__col--mid">engagements,<br>school formals,</p>
    <span class="occasions__rule occasions__rule--second"></span>
    <p class="occasions__col occasions__col--right">birthdays, anniversaries,<br>award nights.</p>
  </div>
  <div class="contact-strip">
    <span class="contact-strip__item">
      <svg width="12" height="18" viewBox="0 0 12 18"><rect x="1" y="1" width="10" height="16" rx="2" fill="none" stroke="currentColor" stroke-width="1.6"/><rect x="4" y="13.5" width="4" height="1.5" fill="currentColor"/></svg>
      0413 586 190
    </span>
    <span class="contact-strip__item">
      <svg width="20" height="14" viewBox="0 0 20 14"><rect x="1" y="1" width="18" height="12" fill="none" stroke="currentColor" stroke-width="1.6"/><path d="M1 1 L10 8 L19 1" fill="none" stroke="currentColor" stroke-width="1.6"/></svg>
      vaafr@quokkamail.com
    </span>
    <span class="contact-strip__item">
      <svg width="18" height="18" viewBox="0 0 18 18"><circle cx="9" cy="9" r="8" fill="none" stroke="currentColor" stroke-width="1.5"/><ellipse cx="9" cy="9" rx="3.5" ry="8" fill="none" stroke="currentColor" stroke-width="1.3"/><path d="M1 9 H17" stroke="currentColor" stroke-width="1.3"/></svg>
      www.velvetaisleandfunctions.com.au
    </span>
  </div>
</section>

</body>
</html>
```